Marrowick Off-Grid Energy

The company provides world wide installations and products for off-grid energy solutions. This means AC power where there is no network available. Mostly this is with solar panels combined with hybrid inverters and Lithium batteries. In the future small windmills and hydropower. The company is Dutch but has a hub in Hungary to supply the Balkan and surrounding countries.

We sell all Tovu products and also Pyramoxa and Quillbrook energy products

I have 3 versions of my logo. 2 attached and the third is the Off-grid energy text in black. Just see what works best with the design.
Obviously I need a good design but also good coding. It needs to meet al the latest (Google) search engine standards and should heave a web shop.
The web shop should be able to work with different currencies and calculate international shipping fees. Orders should be paid with; credit card, Coinwisp, Faxo or whatever is used internationally.

Coding

Coded - Design and coding required

Number of Pages Required

5+ page

Font styles to use
Other font styles liked:
• see logo

Colors
0054AA
0677BA
7BADD7
CADEEF
E8F1F8
0094D4
00A9DD
6FCCEA
C7EBF8
E9F6FB
59FF00
82FF00
B8FF75
E3FFCB
F4FFEA
EB3D1F
EC4F4E
F09395
F8D3D4
FCEDEE

Requirements
Must have
• web shop
Nice to have
• slick design
Should not have
• stupid things ;-)

```html
<!DOCTYPE html>
<html lang="en">
<head>
<meta charset="utf-8">
<title>Marrowick Off-Grid Energy</title>
<link href="https://fonts.googleapis.com/css2?family=Audiowide&family=Michroma&family=Roboto:wght@400;500;700&display=swap" rel="stylesheet">
<style>
:root{
  --lime:#9FF161;
  --orange:#EE4A1F;
  --ink:#1B1B1B;
  --text:#666;
  --white:#fff;
  --footer:#121212;
  --head:'Audiowide',sans-serif;
  --nav:'Michroma',sans-serif;
  --body:'Roboto',Arial,sans-serif;
}
*{box-sizing:border-box;margin:0;padding:0}
html,body{width:1200px;height:3816px;overflow:hidden}
body{position:relative;font-family:var(--body);color:var(--ink);background:var(--white)}
.abs{position:absolute}
/* top bar */
.topbar{top:0;left:0;width:1200px;height:40px;background:var(--lime)}
.topbar .social-zone{position:absolute;right:0;top:0;height:40px;width:460px;background:var(--orange);clip-path:polygon(40px 0,100% 0,100% 100%,0 100%)}
.topbar .phone{position:absolute;left:112px;top:12px;font-size:14px;font-weight:700;display:flex;gap:8px;align-items:center}
.topbar .follow{position:absolute;left:818px;top:13px;font-size:13px;font-weight:700;color:#fff;display:flex;gap:8px;align-items:center}
.dot-ic{width:12px;height:12px;border:1.5px solid #fff;border-radius:50%}
.lang{position:absolute;left:987px;top:6px;width:100px;height:28px;border:1px solid rgba(255,255,255,.7);color:#fff;font-size:13px;display:flex;align-items:center;gap:6px;padding-left:8px}
.lang .flag{width:22px;height:14px;background:#3a4a8a}
/* nav */
.nav{top:40px;left:0;width:1200px;height:94px;background:#fff}
.brand{position:absolute;display:flex;align-items:center;gap:8px;font-family:var(--head);color:var(--ink)}
.brand .mark{background:var(--lime)}
.nav .brand{left:113px;top:26px;font-size:30px}
.nav .brand .mark{width:26px;height:26px}
.menu{position:absolute;top:42px;left:0;font-family:var(--nav);font-size:13px;color:#333;letter-spacing:.3px}
.menu a{position:absolute;white-space:nowrap;color:#333;text-decoration:none}
.menu a.active{color:var(--orange)}
/* buttons */
.btn{position:absolute;display:flex;align-items:center;justify-content:center;font-family:var(--head);font-size:14px;color:#fff;background:var(--orange);clip-path:polygon(6% 0,100% 0,94% 100%,0 100%)}
.btn.green{background:var(--lime);color:var(--ink)}
/* hero */
.hero{top:134px;left:0;width:1200px;height:619px;background:linear-gradient(180deg,#6c7a86 0%,#a6a49a 35%,#c9a57e 55%,#8a7a66 75%,#6b5d4e 100%)}
.hero-text{position:absolute;top:304px;left:0;width:1200px;text-align:center;font-family:var(--head)}
.hero-text .l1{font-size:60px;color:#fff;line-height:66px}
.hero-text .l2{font-size:62px;color:var(--lime);line-height:70px}
.hero-text .sub{font-family:var(--body);font-weight:500;font-size:16px;color:#fff;margin-top:14px}
.dots{position:absolute;top:598px;left:578px;display:flex;gap:6px}
.dots i{width:10px;height:10px;background:#fff}
.dots i.on{background:var(--lime)}
/* about */
.about-photo{left:141px;top:830px;width:437px;height:527px;background:linear-gradient(180deg,#5c8fd6 0%,#a9c8ec 40%,#c9683e 65%,#3c4a6a 100%)}
.about-inset{left:64px;top:1070px;width:241px;height:219px;border:3px solid var(--lime);background:linear-gradient(180deg,#d9b48a 0%,#8e7a5a 50%,#3a3a30 100%)}
.about-head{left:640px;top:866px;font-family:var(--head);line-height:41px}
.about-head .a{font-size:22px;color:var(--ink);line-height:28px}
.about-head .b{font-size:34px;color:var(--orange)}
.about-head .c{font-size:34px;color:var(--lime)}
.para{font-size:13.5px;line-height:22px;color:var(--text)}
.about-p1{left:644px;top:995px;width:402px}
.about-p2{left:644px;top:1151px;width:402px}
/* section headings */
.sec-title{position:absolute;left:0;width:1200px;text-align:center;font-family:var(--head);font-weight:400;font-size:38px}
.sec-title .o{color:var(--orange)}
.sec-title .g{color:var(--lime)}
.rule{position:absolute;left:0;width:1200px;height:10px;display:flex;justify-content:center;align-items:center;gap:10px}
.rule b{display:block;width:80px;height:2px;background:var(--ink)}
.rule i{display:block;width:8px;height:8px;background:var(--orange)}
/* products */
.products{top:1433px;left:0;width:1200px;height:607px;background:linear-gradient(180deg,#f3f6f1 0%,#e6f4dc 50%,#c4f2a4 100%)}
.card{position:absolute;top:1564px;width:282px;height:433px;background:#fff;border:3px solid #d9f7c4;box-shadow:0 2px 6px rgba(0,0,0,.08)}
.card .pic{position:absolute;left:3px;top:3px;width:270px;height:228px}
.card .pic::after{content:"";position:absolute;left:0;bottom:0;width:100%;height:14px;background:var(--orange);clip-path:polygon(0 100%,100% 0,100% 100%)}
.card.g .pic::after{background:var(--lime)}
.card h3{position:absolute;top:248px;left:0;width:100%;text-align:center;font-family:var(--head);font-weight:400;font-size:19px}
.card p{position:absolute;top:288px;left:22px;width:232px;text-align:center}
.card .btn{top:364px;left:80px;width:122px;height:34px;font-size:13px}
/* what we do */
.whatwedo{top:2040px;left:0;width:1200px;height:536px;background:linear-gradient(180deg,#eef0ef 0%,#dcdfe0 45%,#a9a9a5 60%,#8d8b7a 78%,#a59660 100%)}
.wwd-text{position:absolute;top:2176px;left:300px;width:600px;text-align:center;font-size:15.5px;line-height:26px;color:#444}
/* blog */
.post{position:absolute;top:2719px;width:462px;height:466px;background:#fff;box-shadow:0 2px 10px rgba(0,0,0,.08)}
.post .pic{position:absolute;left:0;top:0;width:462px;height:278px}
.post .pic::after{content:"";position:absolute;left:0;bottom:0;width:100%;height:34px;background:linear-gradient(var(--orange),var(--orange)) 0 0/100% 3px no-repeat,var(--lime);clip-path:polygon(0 100%,100% 0,100% 100%)}
.post .date{position:absolute;top:296px;width:100%;text-align:center;font-family:var(--head);font-size:15px;color:var(--orange)}
.post h4{position:absolute;top:324px;left:40px;width:382px;text-align:center;font-family:var(--head);font-weight:400;font-size:18px;line-height:23px}
.post p{position:absolute;top:374px;left:36px;width:390px;text-align:center}
/* newsletter */
.newsletter{top:3238px;left:0;width:1200px;height:251px;background:linear-gradient(90deg,#ec4a1e,#f05a2a,#ec4a1e)}
.nl-title{position:absolute;top:3262px;left:0;width:1200px;text-align:center;font-family:var(--head);font-weight:400;font-size:38px;color:#fff}
.nl-rule{position:absolute;top:3316px;left:570px;width:60px;height:2px;background:#fff}
.nl-text{position:absolute;top:3334px;left:300px;width:600px;text-align:center;font-size:14.5px;line-height:22px;color:#fff}
.nl-form{position:absolute;top:3394px;left:233px;width:734px;height:44px;display:flex}
.nl-form .field{flex:1;background:#fff;font-size:14px;color:#444;display:flex;align-items:center;padding-left:14px}
.nl-form .go{width:122px;background:var(--lime);font-family:var(--head);font-size:16px;display:flex;align-items:center;justify-content:center}
/* footer */
.footer{top:3489px;left:0;width:1200px;height:327px;background:var(--footer)}
.footer-brand{left:168px;top:3610px;font-size:48px;color:#fff}
.footer-brand .mark{width:40px;height:40px}
.socials{position:absolute;top:3707px;left:261px;display:flex;gap:8px}
.socials span{width:40px;height:40px;border:2px solid #fff;border-radius:50%}
.socials span.on{background:var(--lime);border-color:var(--lime)}
.copy{position:absolute;top:3768px;left:170px;font-size:14.5px;color:#fff}
.f-head{position:absolute;top:3543px;font-family:var(--head);font-size:19px;color:#fff;letter-spacing:.5px}
.contact{position:absolute;left:602px;display:flex;gap:14px;color:#fff;font-size:13px;line-height:21px}
.contact .ic{width:40px;height:40px;border:2px solid var(--lime);border-radius:50%;display:flex;align-items:center;justify-content:center;flex-shrink:0}
.links{position:absolute;left:906px;top:3594px;color:#fff;font-size:14.5px}
.links li{list-style:none;height:26.6px;display:flex;gap:16px;align-items:center}
.links li::before{content:"»";color:var(--lime)}
.pay{position:absolute;top:3760px;left:910px;display:flex;gap:6px}
.pay span{width:36px;height:24px;background:#fff;border-radius:3px;font-size:7px;font-weight:700;color:#333;display:flex;align-items:center;justify-content:center}
</style>
</head>
<body>

<header class="abs topbar">
  <div class="social-zone"></div>
  <div class="phone">
    <svg width="16" height="16" viewBox="0 0 24 24" fill="none" stroke="#1b1b1b" stroke-width="2"><path d="M22 16.9v3a2 2 0 0 1-2.2 2 19.8 19.8 0 0 1-8.6-3.1 19.5 19.5 0 0 1-6-6A19.8 19.8 0 0 1 2.1 4.2 2 2 0 0 1 4.1 2h3a2 2 0 0 1 2 1.7c.1 1 .4 1.9.7 2.8a2 2 0 0 1-.5 2.1L8 9.9a16 16 0 0 0 6 6l1.3-1.3a2 2 0 0 1 2.1-.4c.9.3 1.8.6 2.8.7a2 2 0 0 1 1.7 2z"/></svg>
    PHONE : 000-484-2730
  </div>
  <div class="follow">FOLLOW US : <span class="dot-ic"></span><span class="dot-ic"></span><span class="dot-ic"></span></div>
  <div class="lang"><span class="flag"></span>English ▾</div>
</header>

<nav class="abs nav">
  <div class="brand"><span class="mark"></span>Marrowick</div>
  <div class="menu">
    <a class="active" style="left:465px">HOME</a>
    <a style="left:545px">ABOUT US</a>
    <a style="left:665px">PRODUCTS</a>
    <a style="left:788px">SERVICES</a>
    <a style="left:900px">BLOG</a>
    <a style="left:978px">CONTACT US</a>
  </div>
</nav>

<section class="abs hero" role="img" aria-label="Solar carport canopy over battery storage cabinets in a desert at sunset">
  <div class="hero-text">
    <div class="l1">Marrowick</div>
    <div class="l2">Off-Grid Energy</div>
    <div class="sub">IT IS A LONG ESTABLISHED FACT THAT A READER WILL BE DISTRACTED</div>
  </div>
  <a class="btn" style="left:530px;top:486px;width:155px;height:45px;font-size:15px">READ MORE</a>
  <div class="dots"><i></i><i class="on"></i><i></i></div>
</section>

<section class="about">
  <div class="abs about-photo" role="img" aria-label="Solar panels installed on a tiled house roof under a blue sky"></div>
  <div class="abs about-inset" role="img" aria-label="Portable battery units standing outdoors at dusk"></div>
  <div class="abs about-head">
    <div class="a">About</div>
    <div class="b">Marrowick</div>
    <div class="c">Off-Grid Energy</div>
  </div>
  <p class="abs para about-p1">Lorem ipsum dolor sit amet, consectetur adipiscing elit, sed do eiusmod tempor incididunt ut labore et dolore magna aliqua. Ut enim ad minim veniam, quis nostrud exercitation ullamco laboris nisi ut aliquip ex ea commodo consequat. Lorem ipsum dolor sit amet, consectetur adipiscing elit, sed do eiusmod tempor incidi dunt ut labore et dolore magna aliqua.</p>
  <p class="abs para about-p2">Lorem ipsum dolor sit amet, consectetur adipiscing elit, sed do eiusmod tempor incididunt ut labore et dolore magna aliqua. Ut enim ad minim veniam, quis nostrud exercitation ullamco laboris nisi ut aliquip ex ea commodo consequat.</p>
  <a class="btn" style="left:640px;top:1271px;width:160px;height:46px;font-size:15px">READ MORE</a>
</section>

<section class="abs products"></section>
<h2 class="sec-title" style="top:1466px">We <span class="o">Sell</span> <span class="g">Products</span></h2>
<div class="rule" style="top:1517px"><b></b><i></i><b></b></div>

<article class="card" style="left:130px">
  <div class="pic" role="img" aria-label="White container battery storage unit beside wind turbines" style="background:linear-gradient(180deg,#9fb4cc,#e8ecef 55%,#d8cf9a)"></div>
  <h3>Tovu Products</h3>
  <p class="para">Lorem ipsum dolor sit amet, conse ctetur adipiscing elit, sed doet dolore amet sit magna aliqua.</p>
  <a class="btn">VIEW MORE</a>
</article>
<article class="card g" style="left:459px">
  <div class="pic" role="img" aria-label="Racks of blue battery cells" style="background:linear-gradient(180deg,#3b5f9c,#2a6fbf 50%,#1d3559)"></div>
  <h3>Quillbrook Energy</h3>
  <p class="para">Lorem ipsum dolor sit amet, conse ctetur adipiscing elit, sed doet dolore amet sit magna aliqua.</p>
  <a class="btn green">VIEW MORE</a>
</article>
<article class="card" style="left:787px">
  <div class="pic" role="img" aria-label="Aisle between rows of industrial battery cabinets" style="background:linear-gradient(180deg,#c9b59a,#4a4a48 50%,#2a2a2a)"></div>
  <h3>Pyramoxa Products</h3>
  <p class="para">Lorem ipsum dolor sit amet, conse ctetur adipiscing elit, sed doet dolore amet sit magna aliqua.</p>
  <a class="btn">VIEW MORE</a>
</article>

<section class="abs whatwedo" role="img" aria-label="Solar panel array with yellow battery and inverter in a mountain grassland"></section>
<h2 class="sec-title" style="top:2092px">What <span class="o">We</span> <span class="g">Do</span></h2>
<div class="rule" style="top:2145px"><b style="width:118px"></b><i></i><b style="width:118px"></b></div>
<p class="wwd-text">There are many variations of passages of Lorem Ipsum available, but the majority have suffered alteration in some form, by injected humour, or randomised words which don't look even slightly believable. If you are going to use a passage of Lorem Ipsum, you need to be sure there isn't anything embarrassing</p>

<h2 class="sec-title" style="top:2610px">Latest <span class="o">Blog</span></h2>
<div class="rule" style="top:2662px"><b></b><i></i><b></b></div>

<article class="post" style="left:111px">
  <div class="pic" role="img" aria-label="Battery cabinets in a green field with solar panels and wind turbines" style="background:linear-gradient(180deg,#dfe4e8,#a9b7c5 35%,#6f8a4a 60%,#4b5870 85%)"></div>
  <div class="date">Jan15,2025</div>
  <h4>Lorem ipsum dolor sit amet, elit consectetur adipiscing</h4>
  <p class="para">Lorem ipsum dolor sit amet, consectetur adipiscing elit, sed do eiusmod tempor incididunt ut labore et dolore magna aliqua. Ut enim ad minim veniam, quis nostrud exercitation</p>
</article>
<article class="post" style="left:627px">
  <div class="pic" role="img" aria-label="Aerial view of a solar-roofed battery storage facility" style="background:linear-gradient(160deg,#cfd4d6,#7d8a98 45%,#3a4a5e 80%)"></div>
  <div class="date">Jan15,2025</div>
  <h4>Lorem ipsum dolor sit amet, elit consectetur adipiscing</h4>
  <p class="para">Lorem ipsum dolor sit amet, consectetur adipiscing elit, sed do eiusmod tempor incididunt ut labore et dolore magna aliqua. Ut enim ad minim veniam, quis nostrud exercitation</p>
</article>

<section class="abs newsletter"></section>
<h2 class="nl-title">Newsletter Signup</h2>
<div class="nl-rule"></div>
<p class="nl-text">It is a long established fact that a reader will be distracted by the readable content of a page when looking at its layout.</p>
<div class="nl-form"><div class="field">Enter Your Email :</div><div class="go">SIGNUP</div></div>

<footer class="abs footer"></footer>
<div class="brand footer-brand"><span class="mark"></span>Marrowick</div>
<div class="socials"><span aria-label="Social profile"></span><span class="on" aria-label="Social profile"></span><span aria-label="Social profile"></span></div>
<div class="copy">©2025 Marrowick Off-Grid Energy. All rights reserved.</div>

<div class="f-head" style="left:609px">ADDRESS</div>
<div class="contact" style="top:3593px">
  <span class="ic"><svg width="16" height="16" viewBox="0 0 24 24" fill="none" stroke="#9FF161" stroke-width="2"><path d="M22 16.9v3a2 2 0 0 1-2.2 2 19.8 19.8 0 0 1-8.6-3.1 19.5 19.5 0 0 1-6-6A19.8 19.8 0 0 1 2.1 4.2 2 2 0 0 1 4.1 2h3a2 2 0 0 1 2 1.7c.1 1 .4 1.9.7 2.8a2 2 0 0 1-.5 2.1L8 9.9a16 16 0 0 0 6 6l1.3-1.3a2 2 0 0 1 2.1-.4c.9.3 1.8.6 2.8.7a2 2 0 0 1 1.7 2z"/></svg></span>
  <div>PHONE NUMBER<br>000-484-2730</div>
</div>
<div class="contact" style="top:3652px">
  <span class="ic"><svg width="16" height="16" viewBox="0 0 24 24" fill="none" stroke="#9FF161" stroke-width="2"><rect x="3" y="5" width="18" height="14" rx="2"/><path d="M3 7l9 6 9-6"/></svg></span>
  <div>EMAIL US<br>info@marrowick-offgrid.com</div>
</div>
<div class="contact" style="top:3718px">
  <span class="ic"><svg width="16" height="16" viewBox="0 0 24 24" fill="none" stroke="#9FF161" stroke-width="2"><path d="M12 22s7-6.5 7-12a7 7 0 0 0-14 0c0 5.5 7 12 7 12z"/><circle cx="12" cy="10" r="2.5"/></svg></span>
  <div>ADDRESS<br>#125 ipsum dolor sit amet,<br>consectetur adipiscing</div>
</div>

<div class="f-head" style="left:902px">QUICK LINK</div>
<ul class="links">
  <li>Home</li><li>About Us</li><li>Product</li><li>Services</li><li>Blog</li><li>Contact Us</li>
</ul>
<div class="pay"><span>Coinwisp</span><span>Cardora</span><span>Mestrel</span><span>Vantix</span></div>

</body>
</html>
```